Payday Lending App Interface Design

Hello, we are building a payday lending application, Lendoro, that lend people money. I have drafted some of the screens that show the functionalities we have at the moment, please find the screens in attachments.
The elements in the screens are placed just to show what should be included in those screens, it's not necessary to follow the same layout. If you have better design ideas, you are very welcomed to show off your talent.
I think what we want is a style guide so that we can apply the same style to any screens that are similar to the ones I attached. We really like
the style as in the attached image called Style.png. We might want something similar - a simple, clean design yet fun and engaging. Customised graphical elements such as icons, illustrations are preferable.
Apart from the attached screens, we might also need a design for the On Board screen and the Login/Sign Up screen too.
Our logo colour is in yellow and black. Perhaps we will have a similar colour theme. I also attached the logo file, icon-Lendoro.png, if you would like to put it in your design.
Please message me if you need further information.
Regards
Target Market(s)
Young people that doesn't have strong income
Look and feel
Each slider illustrates characteristics of the customer's brand and the style your logo design should communicate.

```html
<!DOCTYPE html>
<html lang="en">
<head>
<meta charset="utf-8">
<title>Lendoro – Loan Progress</title>
<link rel="stylesheet" href="https://fonts.googleapis.com/css2?family=Mulish:wght@400;700;800;900&display=swap">
<style>
  :root {
    --brand-yellow: #F9D20E;
    --ink: #111111;
    --text: #2a2a2a;
    --alert: #E8262B;
    --muted: #B5B5B5;
    --sheet: #FFFFFF;
    --handle: #D6D6D6;
    --chevron: #8E8E8E;
    --chevron-muted: #D0D0D0;
  }
  * { margin: 0; padding: 0; box-sizing: border-box; }
  html, body { width: 1200px; height: 2597px; overflow: hidden; }
  body {
    font-family: "Mulish", sans-serif;
    background: var(--brand-yellow);
    position: relative;
    color: var(--ink);
  }
  .app-screen { position: absolute; inset: 0; overflow: hidden; }

  .brand-name {
    position: absolute; left: 93px; top: 92px;
    font-size: 64px; font-weight: 900; letter-spacing: -1px; color: var(--ink);
  }
  .top-actions { position: absolute; right: 90px; top: 112px; display: flex; gap: 40px; align-items: center; }

  .greeting { position: absolute; left: 220px; top: 340px; }
  .greeting h1 { font-size: 100px; font-weight: 800; line-height: 1; letter-spacing: -1px; }
  .greeting p { font-size: 49px; font-weight: 400; margin-top: 14px; color: var(--text); }

  .hero-art {
    position: absolute; left: 565px; top: 370px; width: 635px; height: 440px;
    background: radial-gradient(ellipse at 75% 55%, #F08A4B 0%, #F6B27E 35%, rgba(249,210,14,0) 70%);
  }

  .progress-sheet {
    position: absolute; left: 0; top: 783px; width: 1200px; height: 1814px;
    background: var(--sheet); border-radius: 116px 116px 0 0;
  }
  .sheet-handle {
    position: absolute; left: 531px; top: 61px; width: 139px; height: 12px;
    border-radius: 6px; background: var(--handle);
  }

  .timeline-rail { position: absolute; left: 0; top: 0; }

  .step { position: absolute; left: 217px; }
  .step-title { font-size: 46px; font-weight: 800; line-height: 1; }
  .step-desc { font-size: 37px; font-weight: 400; line-height: 58px; margin-top: 14px; color: var(--text); }
  .step--alert .step-desc { color: var(--alert); }
  .step--pending .step-title { color: var(--muted); font-weight: 700; }

  .chevron { position: absolute; left: 1035px; }
  .footer-space { position: absolute; bottom: 0; height: 1px; }
</style>
</head>
<body>
<main class="app-screen">
  <div class="brand-name">Lendoro</div>

  <div class="top-actions">
    <svg class="icon-settings" width="60" height="60" viewBox="0 0 24 24" aria-label="Settings">
      <path fill="#111" d="M19.4 13a7.5 7.5 0 0 0 0-2l2.1-1.6-2-3.5-2.5 1a7 7 0 0 0-1.7-1L15 3h-4l-.4 2.9a7 7 0 0 0-1.7 1l-2.5-1-2 3.5L6.6 11a7.5 7.5 0 0 0 0 2l-2.1 1.6 2 3.5 2.5-1a7 7 0 0 0 1.7 1L11 21h4l.4-2.9a7 7 0 0 0 1.7-1l2.5 1 2-3.5zM13 15.5A3.5 3.5 0 1 1 13 8.5a3.5 3.5 0 0 1 0 7z" transform="translate(-1 0)"/>
    </svg>
    <svg class="icon-menu" width="44" height="60" viewBox="0 0 44 60" aria-label="Menu">
      <g fill="#111">
        <circle cx="9" cy="9" r="8"/><circle cx="35" cy="9" r="8"/>
        <circle cx="9" cy="30" r="8"/><circle cx="35" cy="30" r="8"/>
        <circle cx="9" cy="51" r="8"/><circle cx="35" cy="51" r="8"/>
      </g>
    </svg>
  </div>

  <section class="greeting">
    <h1>Hi, Maya!</h1>
    <p>Ready to start your loan?</p>
  </section>

  <div class="hero-art" role="img" aria-label="3D illustration of a smiling red-haired girl waving hello"></div>

  <section class="progress-sheet">
    <div class="sheet-handle"></div>

    <svg class="timeline-rail" width="1200" height="1814" viewBox="0 0 1200 1814">
      <defs>
        <linearGradient id="railFade" x1="0" y1="0" x2="0" y2="1">
          <stop offset="0" stop-color="#111"/>
          <stop offset="1" stop-color="#D8D8D8"/>
        </linearGradient>
      </defs>
      <line x1="154" y1="217" x2="154" y2="1076" stroke="#111" stroke-width="5"/>
      <line x1="154" y1="1076" x2="154" y2="1505" stroke="url(#railFade)" stroke-width="5"/>

      <g class="node done">
        <circle cx="154" cy="217" r="29" fill="#111"/>
        <path d="M141 217l9 9 17-17" fill="none" stroke="#fff" stroke-width="6" stroke-linecap="round" stroke-linejoin="round"/>
      </g>
      <g class="node alert">
        <circle cx="154" cy="380" r="29" fill="var(--alert)"/>
        <path d="M141 380l9 9 17-17" fill="none" stroke="#fff" stroke-width="6" stroke-linecap="round" stroke-linejoin="round"/>
      </g>
      <g class="node done">
        <circle cx="154" cy="728" r="29" fill="#111"/>
        <path d="M141 728l9 9 17-17" fill="none" stroke="#fff" stroke-width="6" stroke-linecap="round" stroke-linejoin="round"/>
      </g>
      <g class="node done">
        <circle cx="154" cy="1076" r="29" fill="#111"/>
        <path d="M141 1076l9 9 17-17" fill="none" stroke="#fff" stroke-width="6" stroke-linecap="round" stroke-linejoin="round"/>
      </g>
      <g class="node pending">
        <circle cx="154" cy="1331" r="29" fill="#BDBDBD"/>
        <path d="M141 1331l9 9 17-17" fill="none" stroke="#fff" stroke-width="6" stroke-linecap="round" stroke-linejoin="round"/>
      </g>
      <g class="node pending">
        <circle cx="154" cy="1505" r="29" fill="#D8D8D8"/>
        <path d="M141 1505l9 9 17-17" fill="none" stroke="#fff" stroke-width="6" stroke-linecap="round" stroke-linejoin="round"/>
      </g>

      <g fill="none" stroke-width="7" stroke-linecap="round" stroke-linejoin="round">
        <path d="M1040 450l28 32-28 32" stroke="var(--chevron)"/>
        <path d="M1040 730l28 32-28 32" stroke="var(--chevron)"/>
        <path d="M1040 1073l28 32-28 32" stroke="var(--chevron)"/>
        <path d="M1040 1311l28 32-28 32" stroke="var(--chevron-muted)"/>
      </g>
    </svg>

    <div class="step" style="top:195px"><div class="step-title">Start</div></div>

    <div class="step step--alert" style="top:357px">
      <div class="step-title">Upload your personal Information</div>
      <div class="step-desc">It seems like your documents ere expired.<br>Upload your document again to get qualified</div>
    </div>

    <div class="step" style="top:705px">
      <div class="step-title">Connect Bank Account</div>
      <div class="step-desc">Link your bank account with Lendoro for<br>transfer and payment</div>
    </div>

    <div class="step" style="top:1053px">
      <div class="step-title">Apply a Loan</div>
      <div class="step-desc">Get your loan that fit to your need</div>
    </div>

    <div class="step step--pending" style="top:1308px"><div class="step-title">Repayments</div></div>
    <div class="step step--pending" style="top:1482px"><div class="step-title">Loan Closed</div></div>
  </section>
</main>
</body>
</html>
```